Design/Build Engineering and Detailing Service 3D Modeling

We are an engineering company in the construction industry. We specialize in designing blueprints for new construction projects such as high rise buildings, hospitals, hotels, public schools, large scale apartment buildings etc.

We want to have a clean, modern, cutting edge design, but it should be clear and easy to navigate. Related videos in the background of the page are a plus. For example The page now has a picture of the harlow creek bridge in san francisco with fog rolling over it and cars driving on the bridge, saying website coming soon. This is played at a faster frame rate. We want to have customer portal to access files, fill out work orders, pay invoices, make suggestions etc.
Updates

Target Market(s)

Los Angeles, San francisco, San Jose, Portland, Seattle, Las Vegas, Denver

Industry/Entity Type

Construction

Coding

Coded - Design and coding required

Number of Pages Required

4 page

Font styles to use
Serif
Sans Serif

Colors
3276b5
0255a3
85acd3
9d9d9d
5c5c5c
ec1f27
000000
fbee3f
00a990

Requirements
Must have
• Work Examples, mission statement, team members, capabilities. Convey the technical aspects of the business in a way that someone can understand the companies capabilities without knowing the technical side of the business.
Nice to have
• Construction related Videos, Downtown city center skylines, clean, modern, concise design.
Should not have
• Overly complex navigation. should not be to busy

```html
<!DOCTYPE html>
<html lang="en">
<head>
<meta charset="utf-8">
<title>Keystrata Design Inc</title>
<link rel="stylesheet" href="https://fonts.googleapis.com/css2?family=Lato:wght@400;700;900&family=Raleway:wght@500;600;700&display=swap">
<style>
:root{
  --blue:#0255a3;
  --blue-mid:#3276b5;
  --blue-soft:#85acd3;
  --red:#ec1f27;
  --grey:#9d9d9d;
  --grey-dark:#5c5c5c;
  --ink:#2b2b2b;
  --band:#ececec;
  --footer:#2a2a2a;
  --footer-base:#1c1c1c;
  --white:#ffffff;
}
*{box-sizing:border-box;margin:0;padding:0}
html,body{width:1200px;height:4196px;overflow:hidden}
body{font-family:"Lato",Arial,sans-serif;color:var(--ink);background:var(--white);position:relative}
section,header,footer{position:absolute;left:0;width:1200px}
.abs{position:absolute}
.section-title{position:absolute;left:0;width:1200px;text-align:center;font-family:"Raleway",Arial,sans-serif;font-weight:600;font-size:36px;color:#222;letter-spacing:.5px}
.section-title b{color:var(--blue);font-weight:700}
.title-rule{position:absolute;left:540px;width:120px;height:2px;background:#bbb}
.title-rule::after{content:"";position:absolute;left:40px;top:-1px;width:40px;height:4px;background:var(--blue)}
.btn{position:absolute;background:var(--red);color:var(--white);font-weight:700;font-size:16px;text-transform:uppercase;display:flex;align-items:center;justify-content:center;letter-spacing:.5px}
.photo{position:absolute}

/* header */
.site-header{top:0;height:154px;background:var(--white);box-shadow:0 2px 6px rgba(0,0,0,.08);z-index:2}
.brand{left:100px;top:22px;display:flex;align-items:center;gap:12px}
.brand-mark{width:54px;height:54px;background:var(--blue)}
.brand-name{font-family:"Lato",sans-serif;font-weight:900;font-size:26px;color:#2b2b2b;line-height:1.05}
.topbar{right:0;top:0;height:44px;display:flex;font-size:17px}
.topbar .mail{display:flex;align-items:center;gap:8px;padding:0 26px;color:#333}
.topbar .phone{display:flex;align-items:center;gap:10px;padding:0 70px 0 36px;background:var(--grey-dark);color:var(--white);font-size:22px;clip-path:polygon(22px 0,100% 0,100% 100%,0 100%)}
.main-nav{left:447px;top:90px;display:flex;align-items:center;font-family:"Raleway",sans-serif;font-weight:700;font-size:19px;color:#333}
.main-nav a{color:inherit;text-decoration:none;padding:8px 14px}
.main-nav .active{background:var(--blue);color:var(--white)}
.main-nav .sep{width:1px;height:16px;background:#ccc;margin:0 48px}

/* hero */
.hero{top:154px;height:512px}
.hero .photo{inset:0;background:linear-gradient(180deg,#3f5a78 0%,#7a6a60 45%,#2f3540 75%,#16181d 100%)}
.hero-copy{left:0;top:168px;width:560px;height:195px;background:linear-gradient(90deg,rgba(0,0,0,.72),rgba(0,0,0,.15))}
.hero-copy h1{position:absolute;left:100px;top:12px;width:440px;font-family:"Lato",sans-serif;font-weight:900;font-size:27px;line-height:1.3;color:var(--white)}
.hero .btn{left:100px;top:316px;width:142px;height:42px}
.dots{left:100px;top:380px;display:flex;gap:8px}
.dots i{width:11px;height:11px;border-radius:50%;background:#bbb;display:block}
.dots i:first-child{background:var(--white)}

/* welcome */
.welcome{top:666px;height:481px}
.welcome p.lead{position:absolute;left:190px;top:134px;width:820px;text-align:center;font-size:16px;line-height:1.68;color:#444}
.pillar{position:absolute;top:285px;display:flex;gap:14px;width:280px}
.pillar .ring{width:70px;height:70px;border-radius:50%;border:3px solid var(--blue);flex:none;display:flex;align-items:center;justify-content:center}
.pillar h3{font-size:17px;font-weight:900;color:#222;margin-top:4px}
.pillar p{font-size:12.5px;line-height:1.3;color:#555}
.welcome .btn{left:527px;top:386px;width:146px;height:44px}

/* services */
.services{top:1147px;height:553px;background:var(--band)}
.service-card{position:absolute;top:148px;width:442px;height:364px;background:var(--white);border:2px solid #444;box-shadow:22px 22px 0 #c4c4c4}
.service-card .photo{left:10px;top:10px;width:418px;height:294px}
.service-card h3{position:absolute;left:0;bottom:14px;width:100%;text-align:center;font-weight:700;font-size:22px;color:var(--blue)}

/* capabilities */
.capabilities{top:1700px;height:532px}
.capabilities .photo{left:100px;top:155px;width:482px;height:248px;background:linear-gradient(180deg,#b9c7d4 0%,#d9dcdc 45%,#8a8f93 75%,#5d6266 100%)}
.play{left:315px;top:253px;width:52px;height:52px;border-radius:50%;border:3px solid var(--white)}
.play::after{content:"";position:absolute;left:19px;top:13px;border-left:17px solid var(--white);border-top:10px solid transparent;border-bottom:10px solid transparent}
.cap-item{position:absolute;left:624px;width:480px;display:flex;gap:22px}
.cap-icon{width:67px;height:67px;background:#3a3a3a;flex:none;display:flex;align-items:center;justify-content:center}
.cap-item h3{font-size:17px;font-weight:900;color:#222;margin:2px 0 6px}
.cap-item p{font-size:13px;line-height:1.35;color:#555}

/* projects */
.projects{top:2232px;height:766px;background:var(--band)}
.project-grid{position:absolute;left:0;top:140px;width:1200px;height:498px;display:grid;grid-template-columns:repeat(4,300px);grid-template-rows:repeat(2,249px)}
.tile{position:relative}
.tile.featured::after{content:"";position:absolute;inset:0;background:rgba(0,0,0,.45)}
.tile-caption{position:absolute;left:0;top:80px;width:100%;text-align:center;color:var(--white);z-index:1}
.tile-caption h3{font-size:21px;font-weight:700}
.tile-caption p{font-size:13px;line-height:1.35;margin-top:8px}
.tile-caption .plus{width:46px;height:46px;border-radius:50%;border:2px solid var(--white);margin:14px auto 0}
.projects .btn{left:516px;top:677px;width:168px;height:46px;border:2px solid #fff;outline:2px solid var(--red)}

/* team */
.team{top:2998px;height:540px}
.member{position:absolute;top:135px;width:215px}
.member .photo{position:relative;width:215px;height:223px;border-radius:50% 50% 46% 46%;background:linear-gradient(180deg,#d8d2cc,#a48a76)}
.member h3{font-size:15px;font-weight:700;color:#222;margin-top:28px}
.member p{font-size:12.5px;line-height:1.35;color:#555;margin-top:8px}
.socials{display:flex;gap:9px;margin-top:12px}
.socials i{width:24px;height:24px;border-radius:50%;background:#cfcfcf;display:block}

/* callback */
.callback{top:3538px;height:288px;background:linear-gradient(90deg,#0a4f96,#1665b5 60%,#2d6fb0)}
.callback h2{position:absolute;left:100px;top:56px;font-family:"Raleway",sans-serif;font-weight:700;font-size:35px;line-height:1.15;color:var(--white)}
.callback p.note{position:absolute;left:100px;top:152px;width:300px;font-size:13px;line-height:1.45;color:#dce8f6}
.callback .form-label{left:459px;top:48px;font-weight:700;font-size:15px;color:var(--white)}
.field{position:absolute;height:42px;width:308px;background:var(--white);font-size:14px;color:#777;padding:0 14px;display:flex;align-items:center}
.callback .btn{left:459px;top:193px;width:160px;height:42px}

/* footer */
.site-footer{top:3826px;height:314px;background:var(--footer);color:#ddd}
.site-footer h4{position:absolute;top:44px;font-family:"Raleway",sans-serif;font-size:21px;font-weight:700;color:var(--white)}
.foot-rule{position:absolute;top:82px;height:1px;background:#555}
.quick-links{left:140px;top:108px;list-style:none;font-size:14px;line-height:2.55}
.quick-links li::before{content:"• "}
.contact-list{left:372px;top:106px;font-size:13px;line-height:1.3;width:230px}
.contact-list div{display:flex;gap:10px;margin-bottom:14px}
.contact-list svg{flex:none}
.site-footer .photo{left:705px;top:81px;width:352px;height:177px;background:linear-gradient(135deg,#cfe0ea,#e8e4d6 50%,#b7d2e4)}
.copyright{top:4140px;height:56px;background:var(--footer-base);color:#bbb;font-size:12px}
.copyright span{position:absolute;left:100px;top:20px}
.copyright .socials{position:absolute;left:951px;top:12px;margin:0;gap:14px}
.copyright .socials i{width:30px;height:30px;background:var(--blue-mid)}
.copyright .socials i:last-child{background:var(--red)}
</style>
</head>
<body>

<header class="site-header">
  <div class="brand abs"><span class="brand-mark"></span><span class="brand-name">KEYSTRATA<br>DESIGN INC</span></div>
  <div class="topbar abs">
    <div class="mail"><svg width="18" height="13" viewBox="0 0 18 13"><rect x="1" y="1" width="16" height="11" fill="none" stroke="#333" stroke-width="1.6"/><path d="M1 1l8 6 8-6" fill="none" stroke="#333" stroke-width="1.6"/></svg>hello@keystratadesign.com</div>
    <div class="phone"><svg width="18" height="18" viewBox="0 0 24 24"><path d="M6.6 10.8a15 15 0 006.6 6.6l2.2-2.2c.3-.3.7-.4 1-.2 1.1.4 2.3.6 3.6.6.6 0 1 .4 1 1V20c0 .6-.4 1-1 1A17 17 0 013 4c0-.6.4-1 1-1h3.5c.6 0 1 .4 1 1 0 1.3.2 2.5.6 3.6.1.3 0 .7-.2 1z" fill="#fff"/></svg>123-456-7890</div>
  </div>
  <nav class="main-nav abs">
    <a class="active" href="#">HOME</a><span class="sep"></span>
    <a href="#">ABOUT US</a><span class="sep"></span>
    <a href="#">SERVICES</a><span class="sep"></span>
    <a href="#">CONTACT US</a>
  </nav>
</header>

<section class="hero">
  <div class="photo" role="img" aria-label="Downtown city skyline of glass towers at dusk"></div>
  <div class="hero-copy abs">
    <h1>We Are A Full Service Engineering &amp; Detailing Firm That Specializes In Complete Plumbing Coordination &amp; Design Services</h1>
  </div>
  <a class="btn" href="#">Get Started</a>
  <div class="dots abs"><i></i><i></i><i></i><i></i></div>
</section>

<section class="welcome">
  <h2 class="section-title" style="top:60px">WELCOME TO KEYSTRATA <b>DESIGN INC</b></h2>
  <div class="title-rule" style="top:114px"></div>
  <p class="lead">Lorem ipsum dolor sit amet, consectetuer adipiscing elit, sed diam nonummy nibh euismod tincidunt ut laoreet dolore magna aliquam erat volutpat. Ut wisi enim ad minim veniam, quis nostrud exerci tation ullamcorper suscipit lobortis nisl ut aliquip ex ea commodo consequat. Duis autem vel eum iriure dolor in hendrerit in vulputate velit esse molestie consequat, vel illum dolore eu feugiat nulla facilisis at vero eros et accumsan et iusto odio dignissim qui blandit praesent luptatum zzril delenit augue duis dolore te feugait nulla facilisi.</p>
  <div class="pillar" style="left:336px">
    <span class="ring"><svg width="38" height="30" viewBox="0 0 38 30"><circle cx="19" cy="8" r="6" fill="#0255a3"/><circle cx="7" cy="12" r="4.5" fill="#0255a3"/><circle cx="31" cy="12" r="4.5" fill="#0255a3"/><path d="M9 29a10 10 0 0120 0z" fill="#0255a3"/><path d="M0 29a7 7 0 0112-4v4zM38 29a7 7 0 00-12-4v4z" fill="#0255a3"/></svg></span>
    <div><h3>OUR MISSION</h3><p>Sed ut perspiciatis unde omnis iste natus error sit voluptatem accusantium.</p></div>
  </div>
  <div class="pillar" style="left:615px">
    <span class="ring"><svg width="38" height="38" viewBox="0 0 38 38"><circle cx="19" cy="19" r="16" fill="none" stroke="#0255a3" stroke-width="3"/><circle cx="19" cy="19" r="9" fill="none" stroke="#0255a3" stroke-width="3"/><circle cx="19" cy="19" r="3" fill="#0255a3"/><path d="M19 19L34 4" stroke="#0255a3" stroke-width="3"/></svg></span>
    <div><h3>OUR VISION</h3><p>Sed ut perspiciatis unde omnis iste natus error sit voluptatem accusantium.</p></div>
  </div>
  <a class="btn" href="#">Read More</a>
</section>

<section class="services">
  <h2 class="section-title" style="top:40px">OUR <b>SERVICES</b></h2>
  <div class="title-rule" style="top:95px"></div>
  <article class="service-card" style="left:140px">
    <div class="photo" role="img" aria-label="Rolled blueprints and drafting tools on a desk" style="background:linear-gradient(160deg,#dbe7f3,#8fb4d8 60%,#4f7fb2)"></div>
    <h3>Design / Build Engineering</h3>
  </article>
  <article class="service-card" style="left:668px">
    <div class="photo" role="img" aria-label="3D model of a building structure with steel framing" style="background:linear-gradient(160deg,#f1f1ef,#c9cfc9 55%,#8d9a8c)"></div>
    <h3>Detailing Service 3D Modelling</h3>
  </article>
</section>

<section class="capabilities">
  <h2 class="section-title" style="top:46px">OUR <b>CAPABILITIES</b></h2>
  <div class="title-rule" style="top:101px"></div>
  <div class="photo" role="img" aria-label="Video still of a modern hospital building with a street crossing"></div>
  <span class="play abs"></span>
  <div class="cap-item" style="top:168px">
    <span class="cap-icon"><svg width="30" height="38" viewBox="0 0 30 38"><circle cx="15" cy="13" r="11" fill="none" stroke="#fff" stroke-width="3"/><path d="M8 22l-3 14 10-5 10 5-3-14" fill="none" stroke="#fff" stroke-width="3"/></svg></span>
    <div><h3>We Deliver Quality</h3><p>Ut wisi enim ad minim veniam, quis nostrud exerci taton mori oli ullamcorper suscipit lobortis nisl ut aliquip.</p></div>
  </div>
  <div class="cap-item" style="top:250px">
    <span class="cap-icon"><svg width="38" height="38" viewBox="0 0 38 38"><circle cx="19" cy="19" r="15" fill="none" stroke="#fff" stroke-width="3"/><path d="M12 19l5 5 9-10" fill="none" stroke="#fff" stroke-width="3"/></svg></span>
    <div><h3>Always On Time</h3><p>Ut wisi enim ad minim veniam, quis nostrud exerci taton mori oli ullamcorper suscipit lobortis nisl ut aliquip.</p></div>
  </div>
  <div class="cap-item" style="top:334px">
    <span class="cap-icon"><svg width="38" height="38" viewBox="0 0 38 38"><circle cx="19" cy="19" r="11" fill="none" stroke="#fff" stroke-width="6" stroke-dasharray="5 3.6"/><circle cx="19" cy="19" r="5" fill="#fff"/></svg></span>
    <div><h3>We Are Passionate</h3><p>Ut wisi enim ad minim veniam, quis nostrud exerci taton mori oli ullamcorper suscipit lobortis nisl ut aliquip.</p></div>
  </div>
  <div class="cap-item" style="top:417px">
    <span class="cap-icon"><svg width="40" height="30" viewBox="0 0 40 30"><circle cx="12" cy="8" r="5" fill="#fff"/><circle cx="28" cy="8" r="5" fill="#fff"/><path d="M3 29a9 9 0 0118 0zM19 29a9 9 0 0118 0z" fill="#fff"/></svg></span>
    <div><h3>Professional Services</h3><p>Ut wisi enim ad minim veniam, quis nostrud exerci taton mori oli ullamcorper suscipit lobortis nisl ut aliquip.</p></div>
  </div>
</section>

<section class="projects">
  <h2 class="section-title" style="top:40px">LATEST <b>PROJECTS</b></h2>
  <div class="title-rule" style="top:95px"></div>
  <div class="project-grid">
    <div class="tile featured" role="img" aria-label="Office block under a cloudy sky" style="background:linear-gradient(180deg,#8e9aa0,#5b6a5e)">
      <div class="tile-caption"><h3>Dollar Consequte</h3><p>Lorem ipsum dolor sit amet, more<br>consectetuer adipiscing elit.</p><div class="plus"></div></div>
    </div>
    <div class="tile" role="img" aria-label="White modern office tower against blue sky" style="background:linear-gradient(180deg,#2e5fa6,#a9bfd8 60%,#e2e6ea)"></div>
    <div class="tile" role="img" aria-label="Glass buildings beside a park pond" style="background:linear-gradient(180deg,#d6e3ee,#8fae78 60%,#4f7a3b)"></div>
    <div class="tile" role="img" aria-label="Contemporary facade with glass panels" style="background:linear-gradient(160deg,#dfe6ec,#9aa3aa 55%,#5e666d)"></div>
    <div class="tile" role="img" aria-label="Brick apartment building on a street" style="background:linear-gradient(180deg,#cfd9e2,#b07d62 55%,#6d5446)"></div>
    <div class="tile" role="img" aria-label="Wood and glass building at dusk" style="background:linear-gradient(180deg,#5a7196,#8b5a3e 55%,#3b2d26)"></div>
    <div class="tile" role="img" aria-label="Timber clad building on a lawn" style="background:linear-gradient(180deg,#c7d5e2,#a0603a 50%,#6e8a48)"></div>
    <div class="tile" role="img" aria-label="Tall brick hotel beside a road" style="background:linear-gradient(180deg,#3a73c0,#c2a18a 55%,#6c6f72)"></div>
  </div>
  <a class="btn" href="#">View All Photos</a>
</section>

<section class="team">
  <h2 class="section-title" style="top:40px">OUR <b>TEAM</b></h2>
  <div class="title-rule" style="top:95px"></div>
  <div class="member" style="left:100px">
    <div class="photo" role="img" aria-label="Portrait of team member Owen Dallard"></div>
    <h3>Mr. Owen Dallard</h3><p>Duis autem vel eum iriure dolor in mori nibh no hendrerit in vulputate.</p>
    <div class="socials"><i></i><i></i><i></i><i></i></div>
  </div>
  <div class="member" style="left:358px">
    <div class="photo" role="img" aria-label="Portrait of team member Tessa Marlow"></div>
    <h3>Mrs. Tessa Marlow</h3><p>Duis autem vel eum iriure dolor in mori nibh no hendrerit in vulputate.</p>
    <div class="socials"><i></i><i></i><i></i><i></i></div>
  </div>
  <div class="member" style="left:618px">
    <div class="photo" role="img" aria-label="Portrait of team member Dario Quell"></div>
    <h3>Mr. Dario Quell</h3><p>Duis autem vel eum iriure dolor in mori nibh no hendrerit in vulputate.</p>
    <div class="socials"><i></i><i></i><i></i><i></i></div>
  </div>
  <div class="member" style="left:875px">
    <div class="photo" role="img" aria-label="Portrait of team member Jenna Lorcan"></div>
    <h3>Miss Jenna Lorcan</h3><p>Duis autem vel eum iriure dolor in mori nibh no hendrerit in vulputate.</p>
    <div class="socials"><i></i><i></i><i></i><i></i></div>
  </div>
</section>

<section class="callback">
  <h2>Request<br>A Call Back.</h2>
  <p class="note">Duis autem vel eum iriure dolorm opl immokl hendi rerit in vulpu totemi velitm assemol mo molestiel consegb ust, velml illum dolor eu no atn nulla more facilisis</p>
  <div class="form-label abs">Please fill up bellow form</div>
  <div class="field" style="left:459px;top:82px">Name</div>
  <div class="field" style="left:792px;top:82px">Email</div>
  <div class="field" style="left:459px;top:143px">Phone</div>
  <div class="field" style="left:792px;top:143px">Message</div>
  <a class="btn" href="#">Submit</a>
</section>

<footer class="site-footer">
  <h4 style="left:140px">Quick Links</h4>
  <div class="foot-rule" style="left:140px;width:150px"></div>
  <ul class="quick-links abs"><li>Home</li><li>About Us</li><li>Services</li><li>Contact Us</li></ul>
  <h4 style="left:372px">Contact Details</h4>
  <div class="foot-rule" style="left:372px;width:220px"></div>
  <div class="contact-list abs">
    <div><svg width="14" height="18" viewBox="0 0 14 18"><path d="M7 0a7 7 0 017 7c0 5-7 11-7 11S0 12 0 7a7 7 0 017-7z" fill="#ddd"/><circle cx="7" cy="7" r="2.5" fill="#2a2a2a"/></svg><span>KEYSTRATA DESIGN INC<br>123 PO Duis aute iriur dolore<br>orependerit amit in voluptate</span></div>
    <div><svg width="14" height="14" viewBox="0 0 24 24"><path d="M6.6 10.8a15 15 0 006.6 6.6l2.2-2.2c.3-.3.7-.4 1-.2 1.1.4 2.3.6 3.6.6.6 0 1 .4 1 1V20c0 .6-.4 1-1 1A17 17 0 013 4c0-.6.4-1 1-1h3.5c.6 0 1 .4 1 1 0 1.3.2 2.5.6 3.6.1.3 0 .7-.2 1z" fill="#ddd"/></svg><span>123-456-7890</span></div>
    <div><svg width="14" height="14" viewBox="0 0 24 24"><path d="M6.6 10.8a15 15 0 006.6 6.6l2.2-2.2c.3-.3.7-.4 1-.2 1.1.4 2.3.6 3.6.6.6 0 1 .4 1 1V20c0 .6-.4 1-1 1A17 17 0 013 4c0-.6.4-1 1-1h3.5c.6 0 1 .4 1 1 0 1.3.2 2.5.6 3.6.1.3 0 .7-.2 1z" fill="#ddd"/></svg><span>123-456-7890</span></div>
    <div><svg width="15" height="11" viewBox="0 0 18 13"><rect x="1" y="1" width="16" height="11" fill="none" stroke="#ddd" stroke-width="1.6"/><path d="M1 1l8 6 8-6" fill="none" stroke="#ddd" stroke-width="1.6"/></svg><span>hello@keystratadesign.com</span></div>
  </div>
  <h4 style="left:705px">Location Map</h4>
  <div class="photo" role="img" aria-label="Street map showing the office location"></div>
</footer>

<footer class="copyright">
  <span>Copyright © 2016 Keystrata Design Inc. All Rights Reserved.</span>
  <div class="socials"><i></i><i></i><i></i><i></i></div>
</footer>

</body>
</html>
```